Readable, Vibrant Large Shop Front Poster for Tutoring School.

Uncluttered design for the windows of our Business.
It needs to be readable from a distance.
It will be split across two windows. I've uploaded a picture of the premises. The poster is unfortunately split in two- see the shopfront photo - It will be in the two Square windows where the balloons are now.
I've also uploaded our logo which will be used as signage/ on the roof and would like the posters to tie in with it.

What we want to stand out
Over all :
That we are a Tutoring School Specializing in Secondary/KTR Studies

On the left hand side:
- 1 hour lessons are $20 with no joining fees or contracts (casual week to week bookings)

The right hand side:
-Weekly Lessons no contracts
-Summer School
-Holiday Program
-Workshops
-KTR EXAM PREP

Need B0 size (1000mm x 1414mm)

Requirements
Must have
• It must have large clear writing.
Nice to have
• a border top and bottom of the logo swirls, We don't need the business name on this poster.
Should not have
• Not a fan of Purple or Lime Green.

```html
<!DOCTYPE html>
<html lang="en">
<head>
<meta charset="utf-8">
<title>Tutoring School Window Posters</title>
<link rel="stylesheet" href="https://fonts.googleapis.com/css2?family=Bebas+Neue&family=Ubuntu:wght@500;700&display=swap">
<style>
  :root {
    --backdrop: #cfcfcf;
    --paper: #ffffff;
    --sky: #1596d8;
    --sky-deep: #0a86cc;
    --title-blue: #1a8fd0;
    --navy: #2a3a92;
    --red: #c8102e;
    --sticker-red: #e0332f;
    --white: #ffffff;
    --rule: rgba(255,255,255,0.07);
    --rule-paper: rgba(70,140,200,0.14);
    --margin-line: rgba(230,90,110,0.35);
  }
  * { margin: 0; padding: 0; box-sizing: border-box; }
  html, body { width: 1200px; height: 844px; overflow: hidden; }
  body { background: var(--backdrop); position: relative; font-family: "Bebas Neue", sans-serif; }

  .poster {
    position: absolute; width: 514px; overflow: hidden;
    background: var(--sky);
    background-image: repeating-linear-gradient(to bottom, transparent 0 14px, var(--rule) 14px 15px);
    box-shadow: 0 4px 14px rgba(0,0,0,0.25);
  }
  .poster::before {
    content: ""; position: absolute; top: 0; bottom: 0; left: 34px; width: 1px;
    background: var(--margin-line); z-index: 3;
  }
  .poster--left { left: 48px; top: 58px; height: 729px; }
  .poster--right { left: 620px; top: 62px; height: 723px; }

  .poster__band { position: absolute; left: 0; right: 0; bottom: 0; background: var(--sky-deep); }
  .poster--left .poster__band { height: 79px; }
  .poster--right .poster__band { height: 53px; }

  .header {
    position: absolute; left: 0; top: 0; width: 100%; height: 218px;
    background: var(--paper);
    background-image: repeating-linear-gradient(to bottom, transparent 0 14px, var(--rule-paper) 14px 15px);
    text-align: center; z-index: 2;
  }
  .header__pointer {
    position: absolute; left: 210px; top: 217px; width: 0; height: 0;
    border-left: 46px solid transparent; border-right: 46px solid transparent;
    border-top: 47px solid var(--paper); z-index: 2;
  }
  .header__title {
    position: absolute; left: 0; right: 0; top: 40px;
    font-size: 68px; line-height: 1; letter-spacing: 5px; color: var(--title-blue); font-weight: 400;
  }
  .header__sub {
    position: absolute; left: 0; right: 0; top: 112px;
    font-size: 36px; line-height: 1; color: var(--navy);
  }
  .header__focus {
    position: absolute; left: 0; right: 0; top: 148px;
    font-size: 60px; line-height: 1; color: var(--red); letter-spacing: 0.5px;
  }

  .icon { position: absolute; border-radius: 14px; background: rgba(255,255,255,0.1); }

  .offer {
    position: absolute; right: 192px; top: 372px; text-align: right;
    font-size: 62px; line-height: 44px; color: var(--white); letter-spacing: 1px;
  }
  .price {
    position: absolute; left: 344px; top: 374px; width: 136px; height: 136px;
    border-radius: 50%; background: var(--sticker-red);
    border: 6px solid #f1f1f1; box-shadow: 0 4px 8px rgba(0,0,0,0.25);
    display: flex; align-items: center; justify-content: center;
    font-family: "Ubuntu", sans-serif; font-weight: 700; font-size: 40px; color: var(--white);
  }

  .terms {
    position: absolute; left: 0; right: 0; bottom: 22px; text-align: center;
    font-family: "Ubuntu", sans-serif; font-weight: 700; color: var(--white); z-index: 2;
  }
  .terms__main { font-size: 21px; line-height: 1.05; }
  .terms__note { font-size: 16px; line-height: 1.1; }

  .poster__sheen { position: absolute; inset: 0; z-index: 0; }

  .services { position: absolute; left: 34px; top: 210px; list-style: none; z-index: 2; }
  .services__item {
    display: flex; align-items: center; height: 40px; margin-bottom: 21px;
    font-size: 35px; letter-spacing: 2px; color: var(--white); white-space: nowrap;
  }
  .services__tick { width: 40px; height: 40px; margin-right: 8px; flex: none; }
</style>
</head>
<body>

<section class="poster poster--left">
  <div class="header">
    <h1 class="header__title">TUTORING SCHOOL</h1>
    <p class="header__sub">SPECIALIZING IN</p>
    <p class="header__focus">SECONDARY/KTR STUDIES</p>
  </div>
  <div class="header__pointer"></div>

  <div class="icon" style="left:38px;top:262px;width:80px;height:104px;" role="img" aria-label="Line icon of a desk globe"></div>

  <p class="offer">1 HOUR<br>LESSONS<br>ARE</p>
  <div class="price">$20</div>

  <div class="icon" style="left:40px;top:570px;width:90px;height:96px;" role="img" aria-label="Line icon of a light bulb"></div>
  <div class="icon" style="left:398px;top:570px;width:88px;height:80px;" role="img" aria-label="Line icon of a pencil"></div>

  <div class="poster__band"></div>
  <div class="terms">
    <p class="terms__main">no joining fees or contacts</p>
    <p class="terms__note">(casual week to week bookings)</p>
  </div>
</section>

<section class="poster poster--right">
  <svg class="poster__sheen" width="514" height="723" viewBox="0 0 514 723" aria-hidden="true">
    <polygon points="180,0 514,0 514,500" fill="rgba(255,255,255,0.06)"/>
  </svg>

  <div class="icon" style="left:188px;top:30px;width:110px;height:116px;" role="img" aria-label="Line icon of a light bulb"></div>

  <ul class="services">
    <li class="services__item">
      <svg class="services__tick" viewBox="0 0 40 40" aria-hidden="true"><circle cx="20" cy="20" r="19" fill="#fff"/><path d="M11 21 L18 28 L30 13" fill="none" stroke="#2a3a92" stroke-width="5" stroke-linecap="round" stroke-linejoin="round"/></svg>
      WEEKLY LESSONS “NO CONTACTS”
    </li>
    <li class="services__item">
      <svg class="services__tick" viewBox="0 0 40 40" aria-hidden="true"><circle cx="20" cy="20" r="19" fill="#fff"/><path d="M11 21 L18 28 L30 13" fill="none" stroke="#2a3a92" stroke-width="5" stroke-linecap="round" stroke-linejoin="round"/></svg>
      SUMMER SCHOOL
    </li>
    <li class="services__item">
      <svg class="services__tick" viewBox="0 0 40 40" aria-hidden="true"><circle cx="20" cy="20" r="19" fill="#fff"/><path d="M11 21 L18 28 L30 13" fill="none" stroke="#2a3a92" stroke-width="5" stroke-linecap="round" stroke-linejoin="round"/></svg>
      HOLIDAY PROGRAM
    </li>
    <li class="services__item">
      <svg class="services__tick" viewBox="0 0 40 40" aria-hidden="true"><circle cx="20" cy="20" r="19" fill="#fff"/><path d="M11 21 L18 28 L30 13" fill="none" stroke="#2a3a92" stroke-width="5" stroke-linecap="round" stroke-linejoin="round"/></svg>
      WORKSHOPS
    </li>
    <li class="services__item">
      <svg class="services__tick" viewBox="0 0 40 40" aria-hidden="true"><circle cx="20" cy="20" r="19" fill="#fff"/><path d="M11 21 L18 28 L30 13" fill="none" stroke="#2a3a92" stroke-width="5" stroke-linecap="round" stroke-linejoin="round"/></svg>
      KTR EXAM PREP
    </li>
  </ul>

  <div class="icon" style="left:374px;top:308px;width:100px;height:102px;" role="img" aria-label="Line icon of a magnifying glass"></div>
  <div class="icon" style="left:66px;top:578px;width:86px;height:86px;" role="img" aria-label="Line icon of a pencil"></div>
  <div class="icon" style="left:340px;top:575px;width:86px;height:126px;" role="img" aria-label="Line icon of a desk globe"></div>

  <div class="poster__band"></div>
</section>

</body>
</html>
```